Documentary Movie Needs a Poster

We need a poster/lobby card for a documentary film made by six filmmakers. Lobby card needs to list name of sponsor, names of filmmakers and (if feasible, but not required) image frames from each of the six sections of the film.

Text should be very readable. OK to have all caps text or upper/lower.

Design comps are OK, these do not need to be print-ready final images.

Target Market(s)

well educated documentary filmgoers

Industry/Entity Type

Movie

Requirements
Must have
• Must contain the following text (please use helvetica neue or similar font).

Please use the following sponsor name:

The
Marlowe Institute for Cinema
presents

Please use the following filmmaker names:

Theodore Pelusky
Robert Nash
Frederick Tamworth
Harold E. F. Pratt
Vincent Lorimer
Danny Frost

Please use the 6 images in archive/zip to create the card.

You can also do text-only versions of the card (no images).

Card needs to be 2:1 aspect ratio (2000px wide x 1000 pixels high)

Names of filmmakers should each be same size (no filmmaker has visual priority over the other).

Colors for text, lines and other design elements should be RED, BLACK and/or WHITE.

Feel free to crop images if you need to.

```html
<!DOCTYPE html>
<html lang="en">
<head>
<meta charset="utf-8">
<title>Marlowe Institute for Cinema presents — 1 Documentary, 6 Filmmakers</title>
<link rel="stylesheet" href="https://fonts.googleapis.com/css2?family=Arimo:wght@700&family=Roboto+Condensed:wght@700&display=swap">
<style>
  :root {
    --black: #000000;
    --ink: #0b0b0b;
    --red: #c3140f;
    --red-deep: #5a0805;
    --red-dark: #2a0302;
    --white: #ffffff;
    --film-mark: #3a3a3a;
  }
  html, body {
    margin: 0;
    padding: 0;
    width: 1200px;
    height: 600px;
    overflow: hidden;
    background: var(--black);
  }
  .card {
    position: relative;
    width: 1200px;
    height: 600px;
    overflow: hidden;
    background: var(--black);
    font-family: "Arimo", "Helvetica Neue", Helvetica, Arial, sans-serif;
  }
  .hero-photo {
    position: absolute;
    left: 0;
    top: 0;
    width: 760px;
    height: 600px;
    background:
      radial-gradient(ellipse 55% 60% at 62% 45%, rgba(20,2,1,0.85) 0%, rgba(20,2,1,0) 70%),
      radial-gradient(ellipse 80% 70% at 35% 40%, #b3140e 0%, #8a0e09 45%, var(--red-dark) 85%, var(--black) 100%);
  }
  .tagline {
    position: absolute;
    display: flex;
    align-items: flex-end;
    gap: 8px;
    line-height: 1;
  }
  .tagline__number {
    color: var(--white);
    font-size: 96px;
    letter-spacing: -4px;
    filter: blur(0.6px);
  }
  .tagline__word {
    font-size: 44px;
    text-transform: uppercase;
    letter-spacing: -1px;
    color: rgba(255,255,255,0.55);
    filter: blur(2px);
    padding-bottom: 12px;
  }
  .tagline--documentary { left: 14px; top: 2px; }
  .tagline--filmmakers { left: 150px; top: 442px; }

  .title {
    position: absolute;
    left: 795px;
    top: 14px;
    margin: 0;
    color: var(--white);
    font-size: 41px;
    line-height: 1.0;
    letter-spacing: -0.5px;
    font-weight: 700;
  }
  .title-rule {
    position: absolute;
    left: 793px;
    top: 190px;
    width: 322px;
    height: 20px;
    background: var(--red);
  }

  .film-strip {
    position: absolute;
    width: 450px;
    height: 116px;
    padding: 17px 12px;
    display: flex;
    gap: 7px;
    background: var(--ink);
    box-shadow: 0 4px 10px rgba(0,0,0,0.6);
    transform: rotate(-9deg);
  }
  .film-strip::before,
  .film-strip::after {
    content: "";
    position: absolute;
    left: 6px;
    right: 6px;
    height: 7px;
    background: repeating-linear-gradient(90deg, var(--film-mark) 0 7px, transparent 7px 14px);
  }
  .film-strip::before { top: 5px; }
  .film-strip::after { bottom: 5px; }
  .strip-one   { left: 50px;  top: 92px; }
  .strip-two   { left: 22px;  top: 256px; }
  .strip-three { left: 555px; top: 228px; }
  .strip-four  { left: 527px; top: 408px; }

  .frame {
    flex: 1;
    height: 116px;
  }
  .frame--name {
    display: flex;
    align-items: center;
    justify-content: center;
    text-align: center;
    background: var(--red);
    color: var(--white);
    font-family: "Roboto Condensed", "Helvetica Neue", Arial, sans-serif;
    font-size: 23px;
    line-height: 1.05;
    padding: 0 8px;
  }
  .frame--still-desert { background: linear-gradient(160deg, #c9c1b2 0%, #9a8e78 55%, #6d6452 100%); }
  .frame--still-wreck  { background: linear-gradient(170deg, #cfc6b6 0%, #a8987c 60%, #7a6a50 100%); }
  .frame--still-rooftop{ background: linear-gradient(170deg, #9aa2a6 0%, #8c7f64 55%, #5b5342 100%); }
  .frame--still-archive{ background: linear-gradient(160deg, #b8b8b8 0%, #7c7c7c 55%, #3e3e3e 100%); }
  .frame--still-crowd  { background: linear-gradient(170deg, #d9d2c4 0%, #8a7a5e 50%, #3f4a2e 100%); }
  .frame--still-protest{ background: linear-gradient(180deg, #8fb6e0 0%, #c9d4de 50%, #3c3a3a 100%); }
</style>
</head>
<body>
<main class="card">
  <div class="hero-photo" role="img" aria-label="Red-toned photograph of a helmeted soldier holding a rifle"></div>

  <div class="tagline tagline--documentary">
    <span class="tagline__number">1</span>
    <span class="tagline__word">Documentary</span>
  </div>
  <div class="tagline tagline--filmmakers">
    <span class="tagline__number">6</span>
    <span class="tagline__word">Filmmakers</span>
  </div>

  <h1 class="title">The<br>Marlowe Institute<br>for Cinema<br>presents</h1>
  <div class="title-rule"></div>

  <div class="film-strip strip-one">
    <div class="frame frame--name">Theodore Pelusky</div>
    <div class="frame frame--still-desert" role="img" aria-label="Film still: soldier kneeling on a dusty road"></div>
    <div class="frame frame--name">Frederick Tamworth</div>
  </div>

  <div class="film-strip strip-two">
    <div class="frame frame--still-wreck" role="img" aria-label="Film still: wrecked armoured vehicle in the desert"></div>
    <div class="frame frame--name">Robert Nash</div>
    <div class="frame frame--still-rooftop" role="img" aria-label="Film still: soldiers on a rooftop above a smoking city"></div>
  </div>

  <div class="film-strip strip-three">
    <div class="frame frame--name">Harold E. F. Pratt</div>
    <div class="frame frame--still-archive" role="img" aria-label="Film still: black and white archive photo of a soldier in rubble"></div>
    <div class="frame frame--name">Danny Frost</div>
  </div>

  <div class="film-strip strip-four">
    <div class="frame frame--still-crowd" role="img" aria-label="Film still: crowd of armed fighters raising rifles"></div>
    <div class="frame frame--name">Vincent Lorimer</div>
    <div class="frame frame--still-protest" role="img" aria-label="Film still: protesters with signs in front of a domed capitol"></div>
  </div>
</main>
</body>
</html>
```